New business card design for Pinecrest Hollow Optometry Clinic

We need a new business card design using our existing logo (uploaded). Please do not include eyes, eye exam charts or beaches, water, sand. The logo I uploaded shows our colors of green and blue, but we are open to seeing it in black OR white. We would like to see something modern and fresh. It will need to be 2 sided. On the front we will need to be able to put a doctors name, for example-Dr Marta Kellerman and Associates. We will need to be able to change the name to other doctors names when we send for printing. The back of the card should list the following: 3817 Tarrow St, Brennholt Falls (P)705-555-0148 (E) info@phoc.ca www.phoc.ca. "We are welcoming new patients" and a line for the appointment date and time. I have uploaded the back of a card to give an example

```html
<!DOCTYPE html>
<html lang="en">
<head>
<meta charset="utf-8">
<title>Pinecrest Hollow Optometry Clinic – Business Card</title>
<link href="https://fonts.googleapis.com/css2?family=Montserrat:wght@400;500;700&display=swap" rel="stylesheet">
<style>
  :root {
    --bg: #2b2b2b;
    --card: #ffffff;
    --green: #1f9a4a;
    --blue: #3e54a3;
    --ink: #3a3a3a;
  }
  * { box-sizing: border-box; margin: 0; padding: 0; }
  html, body { width: 1200px; height: 689px; overflow: hidden; }
  body {
    background: var(--bg);
    font-family: "Montserrat", sans-serif;
    position: relative;
  }
  .card {
    position: absolute;
    top: 190px;
    width: 530px;
    height: 310px;
    background: var(--card);
    border-radius: 22px;
  }
  .card--appointment { left: 50px; }
  .card--contact { left: 620px; }

  /* brand block */
  .brand { display: flex; align-items: center; gap: 10px; }
  .brand__dot {
    width: 18px; height: 18px; border-radius: 50%;
    background: var(--green); flex: none;
  }
  .brand__name {
    color: var(--blue);
    font-weight: 700;
    line-height: 1.2;
  }

  /* appointment side */
  .card--appointment .brand {
    position: absolute; top: 52px; left: 0; right: 0;
    justify-content: center;
  }
  .card--appointment .brand__name { font-size: 20px; }
  .welcome {
    position: absolute; top: 112px; left: 0; right: 0;
    text-align: center;
    color: var(--green);
    font-size: 18px;
    font-weight: 500;
    letter-spacing: 0.3px;
  }
  .field-row {
    position: absolute; left: 48px; right: 48px;
    display: flex; align-items: flex-end; gap: 10px;
    color: var(--green);
    font-size: 17px;
    font-weight: 500;
  }
  .field-row--doctor { top: 180px; }
  .field-row--when { top: 236px; }
  .field__label { white-space: nowrap; }
  .field__line {
    flex: 1;
    border-bottom: 1.5px solid var(--green);
    margin-bottom: 5px;
  }
  .field__label--time { margin-left: 6px; }

  /* contact side */
  .card--contact .brand {
    position: absolute; left: 36px; top: 120px; width: 220px;
  }
  .card--contact .brand__name { font-size: 18px; }
  .divider {
    position: absolute; left: 270px; top: 70px;
    width: 1.5px; height: 170px;
    background: var(--green);
  }
  .details {
    position: absolute; left: 292px; top: 62px; right: 20px;
    color: var(--ink);
  }
  .details__name {
    color: var(--green);
    font-size: 21px;
    font-weight: 700;
    line-height: 1.1;
    white-space: nowrap;
  }
  .details__role { font-size: 15px; margin-top: 2px; }
  .details__address { font-size: 14px; line-height: 1.35; margin-top: 22px; }
  .details__contacts { list-style: none; margin-top: 18px; font-size: 14px; }
  .details__contacts li {
    display: flex; align-items: center; gap: 8px; line-height: 1.45;
  }
  .icon { width: 12px; height: 12px; fill: var(--green); flex: none; }
</style>
</head>
<body>

  <section class="card card--appointment" aria-label="Appointment side">
    <div class="brand">
      <span class="brand__dot"></span>
      <span class="brand__name">Pinecrest Hollow Optometry Clinic</span>
    </div>
    <p class="welcome">We are welcoming new patients!</p>
    <div class="field-row field-row--doctor">
      <span class="field__label">Doctor:</span>
      <span class="field__line"></span>
    </div>
    <div class="field-row field-row--when">
      <span class="field__label">Date:</span>
      <span class="field__line"></span>
      <span class="field__label field__label--time">Time:</span>
      <span class="field__line"></span>
    </div>
  </section>

  <section class="card card--contact" aria-label="Contact side">
    <div class="brand">
      <span class="brand__dot"></span>
      <span class="brand__name">Pinecrest Hollow<br>Optometry Clinic</span>
    </div>
    <div class="divider"></div>
    <div class="details">
      <h1 class="details__name">Dr Marta Kellerman</h1>
      <p class="details__role">Associates</p>
      <p class="details__address">3817 Tarrow St,<br>Brennholt Falls</p>
      <ul class="details__contacts">
        <li>
          <svg class="icon" viewBox="0 0 12 12" aria-hidden="true"><path d="M2.5 0.8 4.3 2.8 3.4 4.2C4.1 5.7 6.3 7.9 7.8 8.6L9.2 7.7 11.2 9.5 10 11.2C5.6 11 1 6.4 0.8 2Z"/></svg>
          <span>705-555-0148</span>
        </li>
        <li>
          <svg class="icon" viewBox="0 0 12 12" aria-hidden="true"><path d="M0.5 2.5H11.5V3.2L6 6.8 0.5 3.2Z"/><path d="M0.5 4.3 6 7.9 11.5 4.3V9.5H0.5Z"/></svg>
          <span>info@phoc.ca</span>
        </li>
        <li>
          <svg class="icon" viewBox="0 0 12 12" aria-hidden="true"><circle cx="6" cy="6" r="5.5"/><path d="M6 0.5V11.5M0.5 6H11.5M2 3H10M2 9H10" stroke="#fff" stroke-width="0.8" fill="none"/></svg>
          <span>www.phoc.ca</span>
        </li>
      </ul>
    </div>
  </section>

</body>
</html>
```